Business Card - Cooperate

Business Card for Larkfield Management Consulting

Target Market(s)

Corparte - b2B

Industry/Entity Type

Management Consulting - Professional Services

Contact Information for Business Card

Company Name , Slogan , Dummy Address,

Requirements
Must have
• Reach your Full Potential

```html
<!DOCTYPE html>
<html lang="en">
<head>
<meta charset="utf-8">
<title>Larkfield Management Consulting – Business Card</title>
<link rel="stylesheet" href="https://fonts.googleapis.com/css2?family=Montserrat:wght@400;500;600;700&display=swap">
<style>
  :root {
    --stage: #2a2b2e;
    --card-white: #ffffff;
    --card-black: #050607;
    --brand-green: #5cbc3c;
    --brand-blue: #2f5fc4;
    --brand-navy: #2b2f7a;
    --text-dark: #3a3a3a;
    --text-muted: #8a8d94;
  }
  * { margin: 0; padding: 0; box-sizing: border-box; }
  html, body { width: 1200px; height: 900px; overflow: hidden; }
  body {
    background: var(--stage);
    font-family: "Montserrat", sans-serif;
    display: flex;
    flex-direction: column;
    align-items: center;
    justify-content: center;
    gap: 60px;
  }
  .card {
    position: relative;
    width: 600px;
    height: 343px;
    border-radius: 18px;
    overflow: hidden;
    box-shadow: 0 10px 30px rgba(0,0,0,.45);
  }
  /* Front */
  .card-front { background: var(--card-white); }
  .corner-tab {
    position: absolute; left: 0; top: 0;
    width: 16px; height: 34px;
    background: var(--brand-navy);
  }
  .holder { position: absolute; left: 40px; top: 28px; }
  .holder-name {
    color: var(--brand-green);
    font-weight: 700; font-size: 22px;
    text-transform: uppercase; letter-spacing: .5px;
  }
  .holder-role { color: var(--text-dark); font-size: 15px; margin-top: 2px; }
  .address {
    position: absolute; left: 40px; top: 160px;
    color: var(--text-dark); font-size: 15px; line-height: 1.35;
    font-style: normal;
  }
  .contacts {
    position: absolute; left: 40px; top: 222px;
    list-style: none; color: var(--text-dark); font-size: 15px; line-height: 1.5;
  }
  .contacts li { display: flex; align-items: center; gap: 7px; }
  .contacts svg { width: 12px; height: 12px; flex: none; }
  .contacts .web { color: var(--brand-navy); }
  .brand { display: flex; align-items: center; gap: 12px; }
  .card-front .brand { position: absolute; right: 40px; bottom: 44px; }
  .brand-dot {
    width: 40px; height: 40px; border-radius: 50%;
    background: var(--brand-green);
  }
  .brand-name {
    color: var(--brand-blue);
    font-weight: 600; font-size: 44px; line-height: 1; letter-spacing: -.5px;
  }
  .slogan {
    color: var(--text-dark);
    font-weight: 400; font-size: 13px;
  }
  .card-front .slogan { position: absolute; right: 40px; top: 34px; }
  /* Back */
  .card-back {
    background: var(--card-black);
    display: flex; align-items: center; justify-content: center;
  }
  .card-back .brand-dot { width: 60px; height: 60px; }
  .card-back .brand-name { font-size: 64px; }
  .card-back .slogan {
    position: absolute; left: 0; right: 0; bottom: 30px;
    text-align: center; color: var(--text-muted);
  }
</style>
</head>
<body>

<section class="card card-front" aria-label="Business card front">
  <div class="corner-tab"></div>
  <div class="holder">
    <p class="holder-name">Daniel Whitmore</p>
    <p class="holder-role">Director</p>
  </div>
  <p class="slogan">Reach your full potential</p>
  <address class="address">
    1187 Birchwood Lane<br>
    Salem, OR 97301
  </address>
  <ul class="contacts">
    <li>
      <svg viewBox="0 0 12 12" aria-hidden="true"><path d="M3 1 L5 3.5 L4 5 Q5 7 7 8 L8.5 7 L11 9 L9.5 11 Q5 11 1 3 Z" fill="var(--brand-navy)"/></svg>
      (555) 214-3090
    </li>
    <li>
      <svg viewBox="0 0 12 12" aria-hidden="true"><rect x="1" y="2.5" width="10" height="7" fill="none" stroke="var(--brand-navy)" stroke-width="1.2"/><path d="M1 2.5 L6 6.5 L11 2.5" fill="none" stroke="var(--brand-navy)" stroke-width="1.2"/></svg>
      info@larkfieldmc.com
    </li>
    <li class="web">
      <svg viewBox="0 0 12 12" aria-hidden="true"><circle cx="6" cy="6" r="5" fill="none" stroke="var(--brand-navy)" stroke-width="1.1"/><ellipse cx="6" cy="6" rx="2.2" ry="5" fill="none" stroke="var(--brand-navy)" stroke-width="1"/><path d="M1 6 H11" stroke="var(--brand-navy)" stroke-width="1"/></svg>
      www.larkfieldmc.com
    </li>
  </ul>
  <div class="brand">
    <span class="brand-dot"></span>
    <span class="brand-name">larkfield</span>
  </div>
</section>

<section class="card card-back" aria-label="Business card back">
  <div class="brand">
    <span class="brand-dot"></span>
    <span class="brand-name">larkfield</span>
  </div>
  <p class="slogan">Reach your full potential</p>
</section>

</body>
</html>
```